PSD for Magento Site (No Code Required)

I Need 10 pages design for a new Plus-Size Lingerie Site. The site has to be a edgy, fun & clean.

I will need versions of each page for mobile, tablet sizes as well. We are trying to be a new kind of lingerie site. something non traditional. A Fun place to show. Big images, Easy Navigation, Simple Layout.

Full Brief is Attached.

Target Market(s)

Plus size Women, Lingerie Enthusiasts

Industry/Entity Type

Retail

Number of Pages Required

5+ page

Font styles to use
Sans Serif

Colors
000000
ffffff
d3d3d3

Requirements
Must have
• Well Structured Mobile versions of each page
Should not have
• clutter

```html
<!DOCTYPE html>
<html lang="en">
<head>
<meta charset="utf-8">
<title>Lushline Lingerie – Chemise</title>
<link href="https://fonts.googleapis.com/css2?family=Montserrat:wght@400;500;600;700&family=Sofia&display=swap" rel="stylesheet">
<style>
:root{
  --ink:#000000;
  --dark:#231f20;
  --white:#ffffff;
  --rule:#d3d3d3;
  --line:#7a7a7a;
  --accent:#f6a04d;
  --script-blue:#8eaed6;
  --slider:#8eaed6;
  --swatch-red:#f0073f;
  --swatch-blue:#1a07f5;
}
*{box-sizing:border-box;margin:0;padding:0}
html,body{width:1200px;height:2287px;overflow:hidden;background:var(--white)}
body{position:relative;font-family:"Montserrat",sans-serif;color:var(--ink)}
.abs{position:absolute}
.site-header{left:0;top:0;width:1200px;height:113px;background:var(--dark)}
.brand{left:62px;top:18px;width:305px;height:55px;background:var(--white);display:flex;align-items:center;justify-content:center;font-weight:600;font-size:30px;letter-spacing:3px;color:var(--dark)}
.top-link{top:43px;font-size:13px;font-weight:500;color:var(--white)}
.search{left:685px;top:26px;width:245px;height:47px;background:var(--white);padding:16px 10px;font-size:12px;color:#b8b8b8}
.icon{top:36px}
.cat-nav{left:0;top:130px;width:1200px;display:flex;justify-content:space-between;padding:0 50px 0 60px;font-size:13px;font-weight:500;text-align:center;line-height:17px}
.promo-line{left:0;top:168px;width:1200px;text-align:center;font-family:"Sofia",cursive;font-size:64px;color:var(--script-blue)}
.crumbs{left:58px;top:282px;font-size:23px;font-weight:500}
.crumbs b{font-weight:700}
.toolbar{top:350px;font-size:17px}
.per-page{left:730px;top:336px;width:51px;height:51px;border:1px solid var(--rule);display:flex;align-items:center;justify-content:center;font-size:18px}
.sort{left:959px;top:336px;width:189px;height:51px;border:1px solid var(--rule);display:flex;align-items:center;justify-content:space-between;padding:0 14px;font-size:17px}
.filters{left:50px;top:0;width:190px}
.f-rule{left:50px;width:188px;height:1px;background:var(--line)}
.f-head{left:52px;font-size:21px;font-weight:600}
.f-text{font-size:22px}
.check{left:52px;width:28px;height:28px;border:1px solid var(--rule)}
.check-on::after{content:"";position:absolute;left:7px;top:7px;width:13px;height:13px;border-radius:50%;background:var(--accent)}
.f-label{left:128px;font-size:22px}
.swatch{top:1213px;width:27px;height:27px}
.slider-track{left:52px;top:1389px;width:193px;height:2px;background:var(--rule)}
.slider-knob{left:131px;top:1380px;width:18px;height:18px;border-radius:50%;background:var(--slider)}
.hero-banner{left:319px;top:410px;width:829px;height:101px;background:linear-gradient(90deg,#2a2624,#4a3a34 55%,#3a2c28);display:flex;align-items:center;justify-content:space-between;padding:0 64px 0 48px}
.hero-title{font-family:"Sofia",cursive;font-size:58px;color:var(--white)}
.shop-link{font-size:21px;font-weight:700;color:var(--white);text-decoration:underline;text-underline-offset:6px}
.product-photo{width:140px;height:340px;background:linear-gradient(180deg,#e9d3c0 0%,#2c2627 35%,#3a3233 70%,#d8bfae 100%)}
.p-name{font-size:23px;font-weight:600}
.p-price{font-size:23px}
.pager{font-size:17px}
.offer{top:1609px;height:255px;color:var(--white);overflow:hidden}
.offer-left{left:50px;width:539px;background:linear-gradient(120deg,#1c2230,#3b3430 55%,#1c2230)}
.offer-right{left:610px;width:538px;background:linear-gradient(120deg,#10182a,#26304a 55%,#111a2c)}
.offer b{position:absolute;font-weight:700}
.site-footer{left:0;top:1897px;width:1200px;height:328px;background:var(--dark);color:var(--white)}
.ft-label{font-size:12px;font-weight:700}
.ft-item{font-size:12px}
.news-input{left:292px;top:1923px;width:320px;height:40px;background:var(--white)}
.news-btn{left:638px;top:1923px;width:127px;height:40px;background:var(--accent);display:flex;align-items:center;justify-content:center;font-family:"Sofia",cursive;font-size:22px;color:var(--white)}
.social{top:1924px;width:38px;height:38px;border-radius:50%;background:var(--white)}
.copyright{left:0;top:2236px;width:1200px;text-align:center;font-size:16px}
</style>
</head>
<body>

<header class="abs site-header"></header>
<div class="abs brand">LUSHLINE</div>
<span class="abs top-link" style="left:465px">STANDARD</span>
<span class="abs top-link" style="left:595px">PLUS SIZE</span>
<div class="abs search">search item</div>
<span class="abs top-link" style="left:959px">LOGIN</span>
<svg class="abs icon" style="left:1010px" width="16" height="20" viewBox="0 0 16 20"><circle cx="8" cy="5" r="4.5" fill="#9fb8d8"/><path d="M0 20 Q0 10 8 10 Q16 10 16 20Z" fill="#9fb8d8"/></svg>
<span class="abs top-link" style="left:1072px">BAG</span>
<svg class="abs icon" style="left:1119px" width="17" height="22" viewBox="0 0 17 22"><path d="M4.5 8 V5 a4 4 0 0 1 8 0 V8" fill="none" stroke="#9fb8d8" stroke-width="2"/><rect x="0" y="8" width="17" height="14" fill="#9fb8d8"/></svg>

<nav class="abs cat-nav">
  <span>LINGERIE</span><span>COSTUMES</span><span>PANTIES</span><span>DRESSES</span><span>SLEEPWEAR</span><span>HOSIERY</span><span>ACCESORIES</span><span>PVC/LEATHER</span><span>HOLIDAY<br>COLLECTION</span><span>SALE</span>
</nav>

<div class="abs promo-line">Free Valentine's Day Shipping Available</div>
<div class="abs crumbs">HOME/LINGERIE/<b>CHEMISE</b></div>

<span class="abs toolbar" style="left:319px">4 items</span>
<span class="abs toolbar" style="left:418px">1</span>
<span class="abs toolbar" style="left:449px">2</span>
<span class="abs toolbar" style="left:479px">&gt;</span>
<span class="abs toolbar" style="left:570px">ITEMS PER PAGE</span>
<div class="abs per-page">24</div>
<span class="abs toolbar" style="left:865px">SORT BY</span>
<div class="abs sort"><span>BEST VALUE</span><span>v</span></div>

<!-- Filters -->
<span class="abs f-text" style="left:52px;top:410px">You've Selected</span>
<span class="abs f-text" style="left:52px;top:464px">Size L</span>
<svg class="abs" style="left:212px;top:467px" width="26" height="26" viewBox="0 0 26 26"><circle cx="13" cy="13" r="11.5" fill="none" stroke="#000" stroke-width="1.2"/><path d="M9 9l8 8M17 9l-8 8" stroke="#000" stroke-width="1.3"/></svg>
<div class="abs f-rule" style="top:537px"></div>

<span class="abs f-head" style="top:559px">Style</span>
<div class="abs check" style="top:604px"></div><span class="abs f-label" style="top:612px">Unlined</span>
<div class="abs check" style="top:658px"></div><span class="abs f-label" style="top:664px">Chemises</span>
<div class="abs f-rule" style="top:759px"></div>

<span class="abs f-head" style="top:806px">Size</span>
<div class="abs check" style="top:853px"></div><span class="abs f-label" style="top:858px">XS</span>
<div class="abs check" style="top:904px"></div><span class="abs f-label" style="top:910px">S</span>
<div class="abs check" style="top:956px"></div><span class="abs f-label" style="top:963px">M</span>
<div class="abs check check-on" style="top:1010px"></div><span class="abs f-label" style="top:1014px">L</span>
<div class="abs check" style="top:1061px"></div><span class="abs f-label" style="top:1068px">XL</span>
<span class="abs" style="left:219px;top:1066px;font-size:18px">x</span>
<div class="abs f-rule" style="top:1135px"></div>

<span class="abs f-head" style="top:1160px">Color</span>
<div class="abs swatch" style="left:52px;background:var(--swatch-red)"></div>
<div class="abs swatch" style="left:102px;background:var(--swatch-blue)"></div>
<div class="abs swatch" style="left:151px;background:var(--white);border:1px solid var(--rule)"></div>
<div class="abs swatch" style="left:202px;background:var(--ink)"></div>
<div class="abs f-rule" style="top:1283px"></div>

<span class="abs f-head" style="top:1313px">Price</span>
<span class="abs f-text" style="left:160px;top:1311px">$25.00</span>
<div class="abs slider-track"></div>
<div class="abs slider-knob"></div>
<span class="abs f-text" style="left:50px;top:1418px">$0</span>
<span class="abs f-text" style="left:195px;top:1418px">$50</span>
<div class="abs f-rule" style="top:1467px"></div>

<!-- Banner -->
<div class="abs hero-banner" role="img" aria-label="Evening photo of a couple behind the Valentine's gifts banner">
  <span class="hero-title">Valentine's Day Gifts</span>
  <span class="shop-link">SHOP NOW</span>
</div>

<!-- Products row 1 -->
<div class="abs product-photo" style="left:319px;top:538px" role="img" aria-label="Model wearing black fringe chemise"></div>
<div class="abs product-photo" style="left:544px;top:538px" role="img" aria-label="Model wearing black fringe chemise"></div>
<div class="abs product-photo" style="left:778px;top:538px" role="img" aria-label="Model wearing black fringe chemise"></div>
<div class="abs product-photo" style="left:1008px;top:538px" role="img" aria-label="Model wearing black fringe chemise"></div>
<span class="abs p-name" style="left:333px;top:896px">Chemise</span><span class="abs p-price" style="left:334px;top:927px">$25.00</span>
<span class="abs p-name" style="left:558px;top:896px">Chemise</span><span class="abs p-price" style="left:560px;top:927px">$25.00</span>
<span class="abs p-name" style="left:790px;top:896px">Chemise</span><span class="abs p-price" style="left:792px;top:927px">$25.00</span>
<span class="abs p-name" style="left:1022px;top:896px">Chemise</span><span class="abs p-price" style="left:1024px;top:927px">$25.00</span>

<!-- Products row 2 -->
<div class="abs product-photo" style="left:319px;top:1052px" role="img" aria-label="Model wearing black fringe chemise"></div>
<div class="abs product-photo" style="left:544px;top:1052px" role="img" aria-label="Model wearing black fringe chemise"></div>
<div class="abs product-photo" style="left:778px;top:1052px" role="img" aria-label="Model wearing black fringe chemise"></div>
<div class="abs product-photo" style="left:1008px;top:1052px" role="img" aria-label="Model wearing black fringe chemise"></div>
<span class="abs p-name" style="left:333px;top:1411px">Chemise</span><span class="abs p-price" style="left:334px;top:1443px">$25.00</span>
<span class="abs p-name" style="left:558px;top:1411px">Chemise</span><span class="abs p-price" style="left:560px;top:1443px">$25.00</span>
<span class="abs p-name" style="left:790px;top:1411px">Chemise</span><span class="abs p-price" style="left:792px;top:1443px">$25.00</span>
<span class="abs p-name" style="left:1022px;top:1411px">Chemise</span><span class="abs p-price" style="left:1024px;top:1443px">$25.00</span>

<span class="abs pager" style="left:316px;top:1523px">1</span>
<span class="abs pager" style="left:348px;top:1523px">2</span>
<span class="abs pager" style="left:377px;top:1523px">&gt;</span>

<!-- Offers -->
<div class="abs offer offer-left" role="img" aria-label="Model in pink corset and jacket for coupon offer">
  <b style="left:28px;top:26px;font-size:40px">FREE</b>
  <b style="left:28px;top:76px;font-size:40px;color:var(--accent)">10%</b>
  <b style="left:28px;top:126px;font-size:40px">OFF</b>
  <b style="left:326px;top:26px;font-size:40px;color:var(--accent)">LUSH10</b>
  <b style="left:10px;top:212px;font-size:21px;font-weight:600">Coupon code applies to items more than $30.</b>
</div>
<div class="abs offer offer-right" role="img" aria-label="Model in blue corset for buy one get one offer">
  <b style="left:10px;top:34px;font-size:33px;line-height:38px">BUY ONE<br>GET ONE</b>
  <b style="left:350px;top:36px;font-size:76px;color:var(--accent)">50%</b>
  <b style="left:450px;top:112px;font-size:28px;color:var(--accent)">OFF</b>
  <b style="left:428px;top:210px;font-size:17px;text-decoration:underline;text-underline-offset:5px">SHOP NOW</b>
</div>

<!-- Footer -->
<footer class="abs site-footer"></footer>
<span class="abs ft-label" style="left:51px;top:1936px;color:var(--white)">SUBSCRIBE TO OUR NEWSLETTER</span>
<div class="abs news-input"></div>
<div class="abs news-btn">Submit</div>
<span class="abs ft-label" style="left:811px;top:1936px;color:var(--white)">FOLLOW US</span>
<div class="abs social" style="left:916px" aria-label="Social link"></div>
<div class="abs social" style="left:1009px" aria-label="Social link"></div>
<div class="abs social" style="left:1090px" aria-label="Social link"></div>

<div style="color:var(--white)">
<span class="abs ft-label" style="left:51px;top:2005px">PRODUCTS</span>
<span class="abs ft-item" style="left:51px;top:2047px">Lingerie</span>
<span class="abs ft-item" style="left:51px;top:2087px">Sexy Costumes</span>
<span class="abs ft-item" style="left:51px;top:2127px">Clearance</span>
<span class="abs ft-item" style="left:51px;top:2166px">Bridal Lingerie</span>
<span class="abs ft-item" style="left:238px;top:2047px">Dresses</span>
<span class="abs ft-item" style="left:238px;top:2087px">Panties</span>
<span class="abs ft-item" style="left:238px;top:2127px">Wigs</span>
<span class="abs ft-item" style="left:238px;top:2168px">Panty Sale</span>
<span class="abs ft-item" style="left:394px;top:2045px">Stockings</span>
<span class="abs ft-item" style="left:394px;top:2085px">Bras</span>
<span class="abs ft-item" style="left:394px;top:2125px">Swimwear</span>

<span class="abs ft-label" style="left:572px;top:2007px">HELP</span>
<span class="abs ft-item" style="left:572px;top:2047px">Customer Service</span>
<span class="abs ft-item" style="left:572px;top:2087px">Live chat</span>
<span class="abs ft-item" style="left:572px;top:2127px">1.000.555.0142</span>
<span class="abs ft-item" style="left:572px;top:2166px">FAQS</span>

<span class="abs ft-label" style="left:810px;top:2005px">ACCOUNT</span>
<span class="abs ft-item" style="left:810px;top:2047px">Your Account</span>
<span class="abs ft-item" style="left:810px;top:2087px">Order Status</span>
<span class="abs ft-item" style="left:810px;top:2127px">Return Authorization</span>
<span class="abs ft-item" style="left:810px;top:2166px">Shipping</span>

<span class="abs ft-label" style="left:1044px;top:2005px">COMPANY</span>
<span class="abs ft-item" style="left:1044px;top:2047px">About Us</span>
<span class="abs ft-item" style="left:1044px;top:2087px">Blog</span>
<span class="abs ft-item" style="left:1044px;top:2127px">Gift Cards</span>
<span class="abs ft-item" style="left:1044px;top:2166px">Privacy Policy</span>
</div>

<div class="abs copyright">©LUSHLINE 2016</div>
</body>
</html>
```